Design a fun and eye catching poster for a Holiday Musical targeted at family and children

The musical is called THE LANTERN PARCEL RACE.
Here is the advertising blurb: In this new holiday musical spectacular, THE LANTERN PARCEL RACE, there is a flurry of activity at the North Pole. Santa and Mrs. Claus, the elves, the reindeer, the forest animals and even the Toys themselves prepare for the biggest night of the year! It takes a lot of planning and hard work to get a sleigh off the ground and to deliver toys to children around the world, but Santa’s team is ready and willing. Or at least they think they are before a tricky Jack Frost decides to stop the Christmas festivities with a little comical chaos and calamity. THE LANTERN PARCEL RACE promises to surprise and delight the young, the young at heart and everyone in between.

So this show is fun, bright, high energy, and tells of the spirit of the Christmas Holiday and the act of giving. Jack Frost is spritely character who tries to freeze Christmas, until is heart is melted. Characters include: Jack Frost, Suzzie Snowflake (sweet and snowy) Santa Claus, Mrs. Claus, SuTap dancing reindeer, busy Christmas elves, animals including a blues singing penguin, a funny squirrel, bunny and a not so smart Polar bear, and three rapping toys- a rag doll, a old-fashioned toy soldier , and a 1950's wind up robot. It takes place at the North Pole in and around Santa's Toy Factory.

We will need the poster to include the following information: THE LANTERN PARCEL RACE Book and Story by Dale Whitcombe, Music by Orrin Pelkey, Lyrics by Marianne Whitcombe

Target Market(s)

Families and children

Industry/Entity Type

Entertainment

Requirements
Must have
• We will need the poster to include the following information: THE LANTERN PARCEL RACE Book and Story by Dale Whitcombe, Music by Orrin Pelkey, Lyrics by Marianne Whitcombe
Nice to have
• I have uploaded images of the production for inspiration. You do not have to include them in the poster. The poster can be artwork or graphic design not necessarily a photo collage.
Should not have
• Do not use the photos... they are just for inspiration. Artwork would be better. Graphic design is preferred over using photos.

```html
<!DOCTYPE html>
<html lang="en">
<head>
<meta charset="utf-8">
<title>The Lantern Parcel Race – The Musical</title>
<link rel="stylesheet" href="https://fonts.googleapis.com/css2?family=Titan+One&family=Nunito:wght@800;900&display=swap">
<style>
  :root {
    --holly-green: #23a24c;
    --holly-green-deep: #15803a;
    --dot-green: #7fcf93;
    --snow-cream: #fbfbe9;
    --cream-dot: #ffffff;
    --berry-red: #e2313d;
    --title-white: #ffffff;
    --credit-white: #ffffff;
  }
  * { margin: 0; padding: 0; box-sizing: border-box; }
  html, body {
    width: 849px;
    height: 1200px;
    overflow: hidden;
    background: var(--snow-cream);
  }
  .poster {
    position: relative;
    width: 849px;
    height: 1200px;
    overflow: hidden;
  }
  .top-band {
    position: absolute;
    left: 0; top: 0;
    width: 849px; height: 113px;
    background: linear-gradient(180deg, var(--holly-green) 0%, #3aae5e 50%, var(--holly-green) 100%);
  }
  .title-panel {
    position: absolute;
    left: 0; top: 113px;
    width: 849px; height: 609px;
    background: radial-gradient(ellipse at 50% 45%, var(--cream-dot) 0%, var(--snow-cream) 70%);
  }
  .bottom-band {
    position: absolute;
    left: 0; top: 722px;
    width: 849px; height: 478px;
    background: linear-gradient(180deg, var(--holly-green) 0%, #35ab59 50%, var(--holly-green) 100%);
  }
  .show-title {
    position: absolute;
    left: 0; top: 190px;
    width: 849px;
    text-align: center;
    font-family: "Titan One", sans-serif;
    font-weight: 400;
    color: var(--berry-red);
    line-height: 1;
    text-transform: uppercase;
  }
  .show-title span {
    display: block;
    text-shadow:
      2px 2px 0 var(--title-white),
      -2px -2px 0 var(--title-white),
      2px -2px 0 var(--title-white),
      -2px 2px 0 var(--title-white),
      -3px 4px 0 var(--holly-green),
      -4px 6px 0 var(--holly-green),
      -5px 8px 0 var(--holly-green),
      -6px 10px 0 var(--holly-green-deep);
  }
  .title-small { font-size: 84px; letter-spacing: 2px; }
  .title-large { font-size: 128px; letter-spacing: 3px; margin-top: 14px; }
  .subtitle {
    position: absolute;
    left: 0; top: 612px;
    width: 849px;
    text-align: center;
    font-family: "Titan One", sans-serif;
    font-style: italic;
    font-size: 54px;
    color: var(--holly-green);
  }
  .credits {
    position: absolute;
    left: 127px; top: 808px;
    list-style: none;
    font-family: "Nunito", sans-serif;
    font-weight: 900;
    font-size: 37px;
    color: var(--credit-white);
    line-height: 1;
  }
  .credits li { margin-bottom: 38px; }
</style>
</head>
<body>
  <main class="poster">
    <div class="top-band" role="img" aria-label="Green band with a light green polka dot pattern"></div>
    <div class="title-panel" role="img" aria-label="Cream panel with a faint white polka dot pattern"></div>
    <div class="bottom-band" role="img" aria-label="Green band with a light green polka dot pattern"></div>

    <h1 class="show-title">
      <span class="title-small">The Lantern</span>
      <span class="title-large">Parcel</span>
      <span class="title-large">Race</span>
    </h1>
    <p class="subtitle">The Musical</p>

    <ul class="credits">
      <li>Book and Story by Dale Whitcombe</li>
      <li>Music by Orrin Pelkey</li>
      <li>Lyrics by Marianne Whitcombe</li>
    </ul>
  </main>
</body>
</html>
```